July 2014 Larkhaven Marketing

Larkhaven Christian Day Schools provide the very best of what you want for your early learner....creative and challenging learning programs, experienced, nurturing teachers with high expectations, spacious, colorful classrooms and exciting opportunities for sharing with family members and the community. We need a postcard design to build enrollment.

Target Market(s)

Parents of children ages 0 to 8

Industry/Entity Type

Marketing

```html
<!DOCTYPE html>
<html lang="en">
<head>
<meta charset="utf-8">
<title>Larkhaven Christian Day Schools – Enrollment Postcard</title>
<link href="https://fonts.googleapis.com/css2?family=Delius&display=swap" rel="stylesheet">
<style>
  :root {
    --backdrop: #2b2b2b;
    --sky-blue: #29abe2;
    --orange: #f47b20;
    --leaf-green: #6cbe45;
    --magenta: #ec0b7f;
    --magenta-dark: #b5095f;
    --lime: #c8dc2c;
    --purple: #a03b97;
    --hill-light: #6aa632;
    --hill-dark: #3f7a1e;
    --cloud-blue: #1fb0ea;
    --paper: #ffffff;
    --rule: #3a3a3a;
    --photo-warm: #e9c6a8;
    --photo-cool: #c9ccd4;
  }
  * { margin: 0; padding: 0; box-sizing: border-box; }
  html, body { width: 1200px; height: 882px; overflow: hidden; background: var(--backdrop); }
  .stage {
    position: relative;
    width: 1200px;
    height: 882px;
    display: flex;
    align-items: center;
    justify-content: center;
    gap: 28px;
  }
  .postcard {
    width: 560px;
    height: 432px;
    display: block;
    box-shadow: 0 6px 18px rgba(0,0,0,.45);
  }
  .school-name {
    font-family: "Delius", cursive;
    fill: var(--paper);
  }
  .front-title { font-size: 28px; }
  .back-title { font-size: 21px; }
  .pitch {
    font-family: "Delius", cursive;
    font-style: italic;
    font-size: 14.5px;
    fill: var(--paper);
  }
  .stripe-blue { fill: var(--sky-blue); }
  .stripe-orange { fill: var(--orange); }
  .stripe-green { fill: var(--leaf-green); }
  .stripe-magenta { fill: var(--magenta); }
  .stripe-lime { fill: var(--lime); }
  .stripe-purple { fill: var(--purple); }
  .cloud-purple { fill: var(--purple); }
  .cloud-blue { fill: var(--cloud-blue); }
  .write-line { stroke: var(--rule); stroke-width: 1.3; }
</style>
</head>
<body>
<main class="stage">

  <!-- Front of the postcard -->
  <svg class="postcard postcard-front" viewBox="0 0 593 457" preserveAspectRatio="none" xmlns="http://www.w3.org/2000/svg">
    <defs>
      <radialGradient id="hill-shade" cx="50%" cy="45%" r="70%">
        <stop offset="0" stop-color="var(--hill-light)"/>
        <stop offset="1" stop-color="var(--hill-dark)"/>
      </radialGradient>
      <linearGradient id="photo-tone" x1="0" y1="0" x2="1" y2="1">
        <stop offset="0" stop-color="var(--photo-warm)"/>
        <stop offset="1" stop-color="var(--photo-cool)"/>
      </linearGradient>
    </defs>

    <g class="rainbow-stripes">
      <rect class="stripe-blue" x="0" y="0" width="99" height="457"/>
      <rect class="stripe-orange" x="99" y="0" width="99" height="457"/>
      <rect class="stripe-green" x="198" y="0" width="99" height="457"/>
      <rect class="stripe-magenta" x="297" y="0" width="99" height="457"/>
      <rect class="stripe-lime" x="396" y="0" width="99" height="457"/>
      <rect class="stripe-purple" x="495" y="0" width="98" height="457"/>
    </g>

    <rect class="cloud-purple cloud-left" role="img" aria-label="Purple cartoon cloud"
          x="40" y="72" width="130" height="72" rx="30"/>
    <rect class="cloud-blue cloud-right" role="img" aria-label="Blue cartoon cloud"
          x="446" y="30" width="112" height="62" rx="26"/>

    <rect class="kids-photo" role="img" aria-label="Photo of six smiling school children leaning in together"
          x="90" y="50" width="405" height="200" rx="40" fill="url(#photo-tone)"/>

    <path class="green-hill" d="M0,345 Q296,215 593,345 L593,457 L0,457 Z" fill="url(#hill-shade)"/>

    <g class="title-ribbon">
      <path d="M22,264 L82,260 L82,314 L22,320 L40,291 Z" fill="var(--magenta-dark)"/>
      <path d="M571,264 L511,260 L511,314 L571,320 L553,291 Z" fill="var(--magenta-dark)"/>
      <path d="M66,242 Q296,222 527,242 L527,298 Q296,278 66,298 Z" fill="var(--magenta)" stroke="var(--magenta-dark)" stroke-width="2"/>
      <text class="school-name front-title" x="296" y="276" text-anchor="middle"
            textLength="420" lengthAdjust="spacingAndGlyphs">Larkhaven Christian Day Schools</text>
    </g>

    <g class="pitch-copy" text-anchor="middle">
      <text class="pitch" x="296" y="332">Creative and challenging learning programs,</text>
      <text class="pitch" x="296" y="354">nurturing teachers with high expectations,experienced,</text>
      <text class="pitch" x="296" y="376">spacious, colorful classrooms and</text>
      <text class="pitch" x="296" y="398">exciting opportunities for sharing with</text>
      <text class="pitch" x="296" y="420">family members and the community.</text>
    </g>
  </svg>

  <!-- Back of the postcard -->
  <svg class="postcard postcard-back" viewBox="0 0 590 457" preserveAspectRatio="none" xmlns="http://www.w3.org/2000/svg">
    <rect class="card-paper" x="0" y="0" width="590" height="457" fill="var(--paper)"/>

    <g class="corner-stripes">
      <rect class="stripe-lime" x="411" y="17" width="82" height="425"/>
      <rect class="stripe-purple" x="493" y="17" width="83" height="425"/>
      <rect class="stripe-magenta" x="326" y="145" width="85" height="297"/>
      <rect class="stripe-green" x="283" y="147" width="43" height="295"/>
      <rect class="stripe-green" x="241" y="378" width="42" height="64"/>
      <rect class="stripe-orange" x="156" y="378" width="85" height="64"/>
      <rect class="stripe-blue" x="73" y="378" width="83" height="64"/>
    </g>

    <rect class="writing-panel" x="295" y="175" width="268" height="200" fill="var(--paper)" fill-opacity="0.62"/>

    <rect class="cloud-purple cloud-panel" role="img" aria-label="Soft purple cartoon cloud"
          x="292" y="155" width="132" height="75" rx="30" fill-opacity="0.55"/>

    <g class="address-lines">
      <line class="write-line" x1="308" y1="197" x2="551" y2="197"/>
      <line class="write-line" x1="308" y1="220" x2="551" y2="220"/>
      <line class="write-line" x1="308" y1="243" x2="551" y2="243"/>
      <line class="write-line" x1="308" y1="266" x2="551" y2="266"/>
      <line class="write-line" x1="308" y1="289" x2="551" y2="289"/>
      <line class="write-line" x1="308" y1="312" x2="551" y2="312"/>
      <line class="write-line" x1="308" y1="335" x2="551" y2="335"/>
      <line class="write-line" x1="308" y1="358" x2="551" y2="358"/>
    </g>

    <rect class="cloud-blue cloud-corner" role="img" aria-label="Light blue cartoon cloud"
          x="452" y="330" width="108" height="52" rx="22" fill-opacity="0.75"/>

    <g class="name-plate">
      <rect x="143" y="390" width="372" height="45" fill="var(--magenta)" stroke="var(--paper)" stroke-width="2.5"/>
      <text class="school-name back-title" x="329" y="419" text-anchor="middle"
            textLength="320" lengthAdjust="spacingAndGlyphs">Larkhaven Christian Day Schools</text>
    </g>
  </svg>

</main>
</body>
</html>
```